Develop a Corporate Identity for Telmo

Telmo is an Australian software start-up business which is targeted to Financial Services professionals. The software has functionality across all areas of financial planning, including customer relationship management, marketing, as well as modelling, document generation and compliance etc.

Our tagline: Powerful, Innovative, Intuitive. The tagline should not overlap the logo or other graphics.

I have attached a mock-up of the logo which I am very pleased with. I am not looking to change this substantially, but am leaving it open for any creative ideas. I am thinking that we might want to include a star on the top-left corner in to reference the Telmo star.

We are looking for the whole suite of Corporate Identity graphics:

- Logo (rectangular and square)
- Favicon
- Business card (template only, details to be filled in later. Include phone, email, address,
- Letterheads (A4, header and footer separated)
- Envelopes (C5)
- Cover page (full A4)
- With compliments slips

Extra points for business cards that stick out, I want people to be interested enough to keep and share them!

All graphics are to be provided in vector format (AI for example) as well as png with transparent background.

```html
<!DOCTYPE html>
<html lang="en">
<head>
<meta charset="utf-8">
<title>Telmo — Business Card</title>
<link rel="stylesheet" href="https://fonts.googleapis.com/css2?family=Montserrat:wght@300;400;500&display=swap">
<style>
  :root{
    --stage:#ecebe8;
    --paper:#f4f4f5;
    --paper-shade:#dcdde0;
    --brand-blue:#1f7fd0;
    --deep-blue:#0d5fae;
    --sky-blue:#2a9ae4;
    --teal:#4fd0dc;
    --white:#ffffff;
    --ink-light:#e8f4ff;
  }
  *{margin:0;padding:0;box-sizing:border-box}
  html,body{width:1200px;height:912px;overflow:hidden;background:var(--stage)}
  body{position:relative;font-family:"Montserrat",Arial,sans-serif}

  .card{position:absolute;width:520px;height:297px;border-radius:3px;overflow:hidden;
        box-shadow:0 10px 24px rgba(0,0,0,.16)}
  .card--front{left:110px;top:130px}
  .card--back{left:570px;top:470px}

  .card__pattern{position:absolute;inset:0;
        background:linear-gradient(135deg,var(--white) 0%,var(--paper) 45%,var(--paper-shade) 100%)}

  .wordmark{position:absolute;font-weight:400;color:var(--brand-blue);letter-spacing:.06em;line-height:1}
  .card--front .wordmark{left:0;right:0;top:104px;text-align:center;font-size:76px}
  .card--front .web{position:absolute;right:34px;bottom:28px;font-size:15px;color:var(--brand-blue)}

  .card--back .wordmark{right:30px;top:34px;font-size:54px}
  .card__shapes{position:absolute;inset:0}

  .holder{position:absolute;left:30px;top:62px;color:var(--white)}
  .holder__name{font-size:17px;font-weight:400;letter-spacing:.08em}
  .holder__role{font-size:9px;letter-spacing:.12em;color:var(--teal);margin-top:3px}

  .contacts{position:absolute;left:30px;top:128px;width:300px;color:var(--ink-light);font-size:12.5px;font-weight:300}
  .contacts__group{padding:7px 0;line-height:1.45}
  .contacts__rule{height:1.5px;background:var(--teal);width:220px}
</style>
</head>
<body>

<section class="card card--front">
  <div class="card__pattern" role="img" aria-label="Subtle light grey triangular pattern background"></div>
  <div class="wordmark">TELMO</div>
  <div class="web">telmo.com.au</div>
</section>

<section class="card card--back">
  <div class="card__pattern" role="img" aria-label="Subtle light grey triangular pattern background"></div>
  <div class="wordmark">TELMO</div>
  <svg class="card__shapes" width="520" height="297" viewBox="0 0 520 297">
    <defs>
      <linearGradient id="bandBlue" x1="0" y1="0" x2="1" y2="1">
        <stop offset="0" stop-color="#2a9ae4"/>
        <stop offset="1" stop-color="#0d5fae"/>
      </linearGradient>
    </defs>
    <polygon points="0,0 190,0 520,210 520,297 0,297" fill="url(#bandBlue)"/>
    <!-- icon tiles -->
    <g fill="#4fd0dc" fill-opacity=".55">
      <rect x="300" y="96" width="70" height="34"/>
      <rect x="370" y="110" width="60" height="34"/>
      <rect x="430" y="140" width="70" height="34"/>
    </g>
    <g fill="none" stroke="#ffffff" stroke-width="1.6" stroke-linecap="round" stroke-linejoin="round">
      <!-- pin -->
      <path d="M318 120c-5-6-7-9-7-12a7 7 0 0 1 14 0c0 3-2 6-7 12z"/><circle cx="318" cy="108" r="2.2"/>
      <!-- phone -->
      <path d="M343 105c1 6 5 10 11 12l2-3-3-2-2 2c-2-1-4-3-5-5l2-2-2-3z"/>
      <!-- mail -->
      <rect x="390" y="119" width="18" height="13"/><path d="M390 119l9 7 9-7"/>
      <!-- signal -->
      <path d="M446 164a6 6 0 0 1 8 0M442 160a12 12 0 0 1 16 0M438 156a18 18 0 0 1 24 0"/>
      <!-- globe -->
      <circle cx="480" cy="157" r="8"/><path d="M472 157h16M480 149c3 3 3 13 0 16M480 149c-3 3-3 13 0 16"/>
    </g>
  </svg>

  <div class="holder">
    <div class="holder__name">MARLOWE</div>
    <div class="holder__role">CEO</div>
  </div>

  <div class="contacts">
    <div class="contacts__group">Ballarat, Australia<br>+61-3-5550-0142</div>
    <div class="contacts__rule"></div>
    <div class="contacts__group">hello@telmo.com</div>
    <div class="contacts__rule"></div>
    <div class="contacts__group">marlowe@telmo.com<br>telmo.com.au</div>
  </div>
</section>

</body>
</html>
```